Business Card design for construction company

I would like a business card design for a construction company - Harlow Constructions. I have attached the ai logo file for use. I would like the card to be very smart and clean and incorporate only white and the two colours in the logo. I would like the card to have two sides. One side can just have the logo, the other with the relevant information.

Target Market(s)

Building and Construction Clients

Industry/Entity Type

Business

Contact Information for Business Card

Name: Tom Pardoe
Company: Harlow Constructions Pty Limited
Address: 14 Mallee Crescent Carrow Vale 2093
Phone: 0427 531 068
Email: tomp@harlowbuild-example.com.au

Font styles to use
Serif
Sans Serif

Requirements
Must have
• Details noted above
• Logo as provided
• Colours as in logo
• Square edges
• A font that compliments the logo
Should not have
• Any colour other than white and those in logo
• Rounded edges

```html
<!DOCTYPE html>
<html lang="en">
<head>
<meta charset="utf-8">
<title>Harlow Constructions – Business Card</title>
<link href="https://fonts.googleapis.com/css2?family=Arimo:wght@400&display=swap" rel="stylesheet">
<style>
  :root {
    --backdrop: #222222;
    --card-light: #f4f4f4;
    --card-dark: #333333;
    --stripe: #4a4a4a;
    --ink: #111111;
    --ink-soft: #1c1c1c;
    --mark: #4d4d4d;
    --accent: #2aa7e0;
  }
  * { margin: 0; padding: 0; box-sizing: border-box; }
  html, body {
    width: 1200px; height: 1000px; overflow: hidden;
    background: var(--backdrop);
    font-family: "Arimo", Arial, sans-serif;
  }
  .canvas { position: relative; width: 1200px; height: 1000px; }

  .card { position: absolute; left: 248px; width: 713px; }

  /* Information side */
  .card-front { top: 38px; height: 425px; background: var(--card-light); }
  .identity {
    position: absolute; left: 0; width: 378px; top: 178px;
    text-align: center; white-space: nowrap;
  }
  .identity-name { font-size: 32px; color: var(--ink); letter-spacing: 0.3px; line-height: 36px; }
  .identity-company { font-size: 17px; color: var(--ink-soft); line-height: 22px; }
  .stripe { position: absolute; left: 358px; top: 0; width: 64px; height: 425px; background: var(--stripe); }
  .contact-icon { position: absolute; left: 376px; width: 28px; height: 32px; }
  .contact-line { position: absolute; left: 436px; font-size: 15px; color: var(--ink); line-height: 20px; white-space: nowrap; }

  /* Logo side */
  .card-back { top: 508px; height: 423px; background: var(--card-dark); }
  .logo-band {
    position: absolute; left: 0; top: 171px; width: 713px; height: 83px;
    background: var(--card-light);
    display: flex; align-items: center; justify-content: center; gap: 14px;
  }
  .logo-dot { width: 10px; height: 10px; border-radius: 50%; background: var(--accent); }
  .logo-name {
    font-size: 27px; letter-spacing: 3px; color: var(--mark);
    text-transform: uppercase;
  }
</style>
</head>
<body>
<div class="canvas">

  <section class="card card-front">
    <div class="identity">
      <p class="identity-name">TOM PARDOE</p>
      <p class="identity-company">Harlow Constructions Pty Limited</p>
    </div>

    <div class="stripe"></div>

    <svg class="contact-icon" style="top:148px" viewBox="0 0 28 32" aria-hidden="true">
      <path d="M14 2a10 10 0 0 0-10 10c0 7.5 10 18 10 18s10-10.5 10-18A10 10 0 0 0 14 2z" fill="#000"/>
      <circle cx="14" cy="12" r="4.2" fill="#fff"/>
    </svg>
    <p class="contact-line" style="top:153px">14 Mallee Crescent Carrow Vale 2093</p>

    <svg class="contact-icon" style="top:196px" viewBox="0 0 28 32" aria-hidden="true">
      <path d="M8 3c2 0 3.5 4.5 3.5 6s-2.5 2-2 4c.8 3 3 6.5 5.5 8.5 1.5 1 2.5-1.5 4-1.5s5 2.5 5 4-2.5 4.5-5 4.5C11 28.5 4 17 4 9c0-3 2-6 4-6z" fill="none" stroke="#fff" stroke-width="1.8"/>
    </svg>
    <p class="contact-line" style="top:203px">0427 531 068</p>

    <svg class="contact-icon" style="top:243px" viewBox="0 0 28 32" aria-hidden="true">
      <g fill="none" stroke="#fff" stroke-width="1.6">
        <circle cx="14" cy="16" r="11"/>
        <ellipse cx="14" cy="16" rx="5" ry="11"/>
        <line x1="3" y1="16" x2="25" y2="16"/>
        <line x1="14" y1="5" x2="14" y2="27"/>
        <path d="M5 10h18M5 22h18"/>
      </g>
    </svg>
    <p class="contact-line" style="top:251px">tomp@harlowbuild-example.com.au</p>
  </section>

  <section class="card card-back">
    <div class="logo-band">
      <span class="logo-dot"></span>
      <span class="logo-name">Harlow Constructions</span>
    </div>
  </section>

</div>
</body>
</html>
```